NEED A BUSINESS CARD FOR A NEW ELECTRICAL BUSINESS

HI I am after a new business card for my new electrical business I have a logo that I have attached its the one in blue, I would like that on the front and on the back my name- Marcus fell, Email marcusfell@tralvinet.com, mobile 0491570156, licence no# vic 48107, nsw 315042k I wont something that is a stand out from the rest but at the same time is neat as being a new business I wont it to catch peoples eye on the front of the card I would like the logo and not much else.
And on the back as well I would like a slogan saying something like
Quality-Reliable-Service

Hi all on the back of the card I would like a little slogan like Quality-Reliable-Service something like that would be good thanks

Hi all the business card needs to have both these licence numbers on it                                                  VIC-48107 nsw-315042k

```html
<!DOCTYPE html>
<html lang="en">
<head>
<meta charset="utf-8">
<title>Marcus Fell Electrical – Business Card, Front and Back</title>
<link href="https://fonts.googleapis.com/css2?family=Arimo:wght@400;700&display=swap" rel="stylesheet">
<style>
  :root {
    --page-bg: #e9e6e1;
    --card-dark: #1c1c1d;
    --card-mid: #343436;
    --brand-blue: #2a8fd8;
    --brand-blue-light: #3aa6ea;
    --silver: #c9cacc;
    --text-light: #f2f2f2;
    --text-muted: #9a9a9c;
    --divider: #58585b;
  }
  * { margin: 0; padding: 0; box-sizing: border-box; }
  html, body {
    width: 1200px;
    height: 576px;
    overflow: hidden;
    background: var(--page-bg);
    font-family: "Arimo", Arial, sans-serif;
  }
  .card {
    position: absolute;
    top: 134px;
    width: 540px;
    height: 308px;
    border-radius: 4px;
    background: radial-gradient(ellipse at 58% 40%, var(--card-mid) 0%, var(--card-dark) 70%);
    box-shadow: 0 10px 30px rgba(0,0,0,0.25);
    overflow: hidden;
  }
  .card-front { left: 40px; }
  .card-back { left: 620px; }

  .brand {
    display: flex;
    align-items: center;
    gap: 10px;
  }
  .brand-square {
    width: 26px;
    height: 26px;
    background: var(--brand-blue);
    flex: none;
  }
  .brand-name {
    font-weight: 700;
    font-size: 19px;
    letter-spacing: 1.5px;
    color: var(--silver);
    text-transform: uppercase;
    white-space: nowrap;
  }
  .licence {
    font-size: 12px;
    font-weight: 700;
    color: var(--brand-blue);
    letter-spacing: 0.3px;
    white-space: nowrap;
  }

  /* Front: logo area only */
  .card-front .front-lockup {
    position: absolute;
    inset: 0;
    display: flex;
    flex-direction: column;
    align-items: center;
    justify-content: center;
    gap: 14px;
  }

  /* Back: details */
  .card-back .brand {
    position: absolute;
    left: 170px;
    top: 58px;
  }
  .card-back .licence {
    position: absolute;
    left: 206px;
    top: 98px;
  }
  .owner {
    position: absolute;
    left: 40px;
    top: 178px;
    font-size: 17px;
    letter-spacing: 0.4px;
    text-transform: uppercase;
    white-space: nowrap;
  }
  .owner-first { font-weight: 700; color: var(--brand-blue-light); }
  .owner-last { font-weight: 400; color: var(--text-muted); }
  .divider {
    position: absolute;
    left: 200px;
    top: 172px;
    width: 1px;
    height: 56px;
    background: var(--divider);
  }
  .contact {
    position: absolute;
    left: 216px;
    top: 176px;
    list-style: none;
    color: var(--text-light);
    font-size: 14px;
  }
  .contact li {
    display: flex;
    align-items: center;
    gap: 12px;
    height: 25px;
    white-space: nowrap;
  }
  .contact .phone-number { font-weight: 700; }
  .contact svg { width: 12px; height: 12px; fill: var(--brand-blue-light); flex: none; }
  .slogan {
    position: absolute;
    left: 0;
    right: 0;
    bottom: 26px;
    text-align: center;
    font-size: 12px;
    font-weight: 700;
    letter-spacing: 3px;
    color: var(--brand-blue);
    text-transform: uppercase;
  }
</style>
</head>
<body>
  <section class="card card-front" aria-label="Card front">
    <div class="front-lockup">
      <div class="brand">
        <span class="brand-square"></span>
        <span class="brand-name">Marcus Fell Electrical</span>
      </div>
      <p class="licence">licence no# vic 48107, nsw 315042k</p>
    </div>
  </section>

  <section class="card card-back" aria-label="Card back">
    <div class="brand">
      <span class="brand-square"></span>
      <span class="brand-name">Marcus Fell Electrical</span>
    </div>
    <p class="licence">licence no# vic 48107, nsw 315042k</p>

    <p class="owner"><span class="owner-first">Marcus</span> <span class="owner-last">Fell</span></p>
    <span class="divider"></span>
    <ul class="contact">
      <li>
        <svg viewBox="0 0 24 24" aria-hidden="true"><path d="M6.6 10.8a15.1 15.1 0 0 0 6.6 6.6l2.2-2.2c.3-.3.7-.4 1-.2 1.1.4 2.3.6 3.6.6.6 0 1 .4 1 1V20c0 .6-.4 1-1 1A17 17 0 0 1 3 4c0-.6.4-1 1-1h3.5c.6 0 1 .4 1 1 0 1.3.2 2.5.6 3.6.1.3 0 .7-.2 1z"/></svg>
        <span class="phone-number">049 157 0156</span>
      </li>
      <li>
        <svg viewBox="0 0 24 24" aria-hidden="true"><path d="M2 5h20v14H2z M3 6l9 7 9-7"/></svg>
        <span class="email">marcusfell@tralvinet.com</span>
      </li>
    </ul>
    <p class="slogan">Quality – Reliable – Service</p>
  </section>
</body>
</html>
```